Canned fish maker looking to improve the graph of his product

We need to refresh the graphic of our product: preserved sardines with vegetable oil to VORELTA brand This product is intended for export to the African market and we must keep the 3 colors Red Gold and Black. The main color is red, gold comes next and black is mostly for text. Red is very important for this product and for this market. There are several brands of different manufacturers (all red gold and black) on the market and the competition is very tough.
Updates

Dear Sirs, I want to design in the same graphic style as the old one but better. Please check the other brand design samples I feel in my project Thanks

Target Market(s)

Canned sardine consumer

Font styles to use
Decorative

Colors
ec1f27
fbed22

Requirements
Must have
• Fish photo Color red gold and black
Nice to have
• product information in different languages
Should not have
• Ps more than 3 colors indicated

```html
<!DOCTYPE html>
<html lang="en">
<head>
<meta charset="utf-8">
<title>VORELTA Sardines – Can Lid Label</title>
<link rel="stylesheet" href="https://fonts.googleapis.com/css2?family=Open+Sans:wght@400;500&family=Caprasimo&family=Alegreya+Sans:wght@400&display=swap">
<style>
  :root {
    --can-red: #d8262b;
    --ink-black: #0a0a0a;
    --window-white: #ffffff;
    --page-bg: #ffffff;
    --glow-pink: #f7cfc6;
    --placeholder-light: #ededed;
    --placeholder-mid: #d6d6d6;
  }
  html, body {
    margin: 0;
    padding: 0;
    width: 1200px;
    height: 788px;
    overflow: hidden;
    background: var(--page-bg);
  }
  .label-canvas {
    display: block;
    width: 1200px;
    height: 788px;
  }
  .lid-body { fill: var(--can-red); }
  .cert-badge { fill: none; stroke: var(--ink-black); stroke-width: 1.6; }
  .brand-name {
    font-family: "Open Sans", sans-serif;
    font-weight: 500;
    font-size: 70px;
    fill: var(--ink-black);
  }
  .net-weight {
    font-family: "Open Sans", sans-serif;
    font-size: 24px;
    fill: var(--ink-black);
  }
  .product-name {
    font-family: "Caprasimo", serif;
    font-size: 64px;
    fill: var(--ink-black);
    stroke: var(--glow-pink);
    stroke-width: 4px;
    paint-order: stroke fill;
  }
  .product-detail {
    font-family: "Alegreya Sans", sans-serif;
    font-size: 22px;
    fill: var(--ink-black);
  }
</style>
</head>
<body>
<svg class="label-canvas" viewBox="0 0 1200 788" xmlns="http://www.w3.org/2000/svg">
  <defs>
    <radialGradient id="window-shade" cx="50%" cy="50%" r="50%">
      <stop offset="90%" stop-color="#ffffff"/>
      <stop offset="100%" stop-color="#c4c4c4"/>
    </radialGradient>
    <linearGradient id="placeholder-tone" x1="0" y1="0" x2="0" y2="1">
      <stop offset="0%" stop-color="#ededed"/>
      <stop offset="100%" stop-color="#d9d9d9"/>
    </linearGradient>
    <filter id="name-glow" x="-10%" y="-30%" width="120%" height="160%">
      <feGaussianBlur in="SourceAlpha" stdDeviation="3" result="blur"/>
      <feFlood flood-color="#f7cfc6"/>
      <feComposite in2="blur" operator="in" result="glow"/>
      <feMerge><feMergeNode in="glow"/><feMergeNode in="SourceGraphic"/></feMerge>
    </filter>
  </defs>

  <rect class="lid-body" x="208" y="184" width="695" height="402" rx="135" ry="135"/>

  <circle class="cert-badge" cx="320" cy="241" r="39"/>

  <text class="brand-name" x="555" y="258" text-anchor="middle" textLength="322" lengthAdjust="spacing">VORELTA</text>
  <text class="net-weight" x="773" y="264">125G</text>

  <ellipse cx="550" cy="367" rx="256" ry="93" style="fill:url(#window-shade)"/>

  <rect class="fish-placeholder" role="img" aria-label="Black and white engraved sardine illustration goes here"
        x="340" y="285" width="445" height="165" rx="24" ry="24" style="fill:url(#placeholder-tone)"/>

  <text class="product-name" x="552" y="526" text-anchor="middle" textLength="362" lengthAdjust="spacingAndGlyphs" filter="url(#name-glow)">SARDINES</text>
  <text class="product-detail" x="546" y="557" text-anchor="middle" textLength="352" lengthAdjust="spacingAndGlyphs">IN VEGETABLE OIL | A L'HUILE VEGETALE</text>
</svg>
</body>
</html>
```